Kolibri-Stube
Ich bin sehr zufrieden mit dem Flyer, Plakat und Logo, welches ich für einen zahlbaren Preis bekommen habe. quorvix hat die Korrekturvorschläge sehr gut und immer zügig umgesetzt und ein wirklich gelungenes Resultat produzier.
Zielgruppe
Logo/Sloagan: Kolibri-Stube
Branchen: Kunst/Kultur und Bildung
Ich biete eine Kolibri-Stube an, in der bis 12 Personen quartalsweise über ein Jahr hinweg an einer Erzählung ode einem Roman arbeiten. Das Genre kann frei gewählt werden. Ob Kriminal-, Fantasy oder Liebesroman, Autobiografie oder Dokufiktion, die Grundlagen eines spannenden Textes sind die selben.
Zielgruppe sind Jugendliche bis Senioren, die gerne eine lägere Erzählung oder einen Roman schreiben möchten.
Aufgabenstellung
Siehe Design-Briefing (PDF) mit Inhalt für Flyertext
Wichtig ist mir der Flyer A4 gefaltet (zu A5 oder 2x gefaltet) oder A5, alle beidseits bedruckt und je nachdem, wie sie den Inhalt verteilen möchten.
Ich bin offen für Design- und Formatvorschläge.
- Ein Plakat A4/A3, welches mit der Vorderseite des Flyers grösstenteils übereinstimmt. Wenn ich ein InDesign oder Photoshop mit Layern kriege, kann ich den Text des Plakats selber ergänzen/bearbeiten.
Ich habe neben dem Briefing und einem Foto von mir noch ein paar Bilder hochgeladen, deren Stil mir gefällt. Habe aber NICHT deren Rechte. Bilder müssten also durch Sie gefunden werden, ich kann diese aber extra bezahlen, bitte Preis dafür deklarieren.
Logo brauche ich noch keines.
Besten Dank für Ihre Bemühungen

```html
<!DOCTYPE html>
<html lang="de">
<head>
<meta charset="utf-8">
<title>Kolibri-Stube – Flyer</title>
<link href="https://fonts.googleapis.com/css2?family=Yanone+Kaffeesatz:wght@300;400;700&display=swap" rel="stylesheet">
<style>
  :root{
    --red-dark:#4a0002;
    --red-mid:#7c0306;
    --red-light:#8c1717;
    --paper:#ffffff;
    --ink:#111111;
    --gold:#e7b416;
    --rose:#e8bcbc;
    --fold:#a33a3a;
  }
  html,body{margin:0;padding:0;width:1200px;height:848px;overflow:hidden;}
  .flyer{
    position:relative;width:1200px;height:848px;overflow:hidden;
    font-family:"Yanone Kaffeesatz",sans-serif;font-weight:300;color:var(--ink);
    background:
      repeating-linear-gradient(225deg,
        var(--red-dark) 0 170px,
        var(--red-light) 170px 330px,
        var(--red-mid) 330px 400px,
        var(--red-dark) 400px 560px);
  }
  .fold{position:absolute;top:0;width:1px;height:848px;background:var(--fold);opacity:.6;}
  .fold--a{left:392px}.fold--b{left:796px}

  /* left panel */
  .intro-card{position:absolute;left:21px;top:65px;width:351px;height:759px;background:var(--paper);box-sizing:border-box;padding:0 6px 0 7px;}
  .question{font-size:26px;line-height:31px;margin:0;}
  .question b{font-weight:700;}
  .question .r{text-align:right;display:block;}
  .q1{margin-top:40px}.q2{margin-top:40px}.q3{margin-top:40px}.q4{margin-top:40px}
  .body-copy{font-size:13.6px;line-height:17px;margin:0;text-align:justify;}
  .body-copy.first{margin-top:20px}
  .body-copy + .body-copy{margin-top:17px}
  .body-copy strong{font-weight:700;}

  /* middle panel */
  .ornament{position:absolute;background:radial-gradient(circle,rgba(231,180,22,.35),rgba(231,180,22,0) 70%);}
  .ornament--url-left{left:412px;top:226px;width:52px;height:52px;}
  .ornament--url-right{left:722px;top:236px;width:52px;height:52px;}
  .ornament--corner{left:1126px;top:774px;width:52px;height:52px;}
  .ornament--logo{left:816px;top:20px;width:34px;height:50px;}
  .web{position:absolute;left:430px;top:234px;width:330px;margin:0;text-align:center;color:#fff;font-size:36px;line-height:46px;letter-spacing:.3px;}
  .portrait{position:absolute;left:655px;top:592px;width:104px;height:140px;background:linear-gradient(160deg,#e9ece4,#b9a48e 55%,#5fc6d0);}
  .trainer{position:absolute;left:412px;top:717px;width:363px;height:111px;background:var(--rose);box-sizing:border-box;padding:6px 7px;font-size:13.4px;line-height:17px;text-align:justify;}
  .trainer strong{font-weight:700;}

  /* right panel */
  .logo-box{position:absolute;left:820px;top:23px;width:268px;height:409px;background:var(--paper);border:2px solid #000;box-sizing:border-box;}
  .logo-name{position:absolute;left:22px;top:44px;margin:0;font-weight:400;font-size:68px;line-height:82px;letter-spacing:7px;color:var(--ink);}
  .quill-area{position:absolute;left:1020px;top:172px;width:160px;height:232px;background:linear-gradient(200deg,rgba(255,255,255,.9),rgba(231,180,22,.45));}
  .tagline{position:absolute;left:886px;top:442px;color:#fff;font-size:25px;line-height:31px;font-weight:400;margin:0;}
  .tagline span{display:block}
  .tagline span+span{padding-left:36px}
</style>
</head>
<body>
<main class="flyer">
  <div class="fold fold--a"></div>
  <div class="fold fold--b"></div>

  <section class="intro-card">
    <p class="question q1">Haben Sie eine erste <b>Idee</b> für eine<span class="r">Erzählung oder einen Roman?</span></p>
    <p class="question q2">&emsp;&emsp;Eine lebhafte <b>Fantasie</b> für das<br>Ausserordentliche oder<span class="r"><b>ungewöhnlich Gewöhnliche</b>?</span></p>
    <p class="question q3">Oder ein <b>reiches Leben</b>,<span class="r">aus dessen Quelle Sie für&ensp;</span>&ensp;Ihre Geschichte schöpfen können?</p>
    <p class="question q4">Und möchten Sie den zukünftigen<span class="r">Leserinnen und Lesern Ihren&ensp;</span><b>geistigen Schatz in Form eines Buches</b><span class="r">schenken?&ensp;</span></p>
    <p class="body-copy first">Dann schreiben Sie Ihren ersten eigenen Roman!<br>Ein erster Ideenfaden spinnt sich in Ihren Gedanken und vielleicht haben Sie diesen schon zu Papier gebracht. Aber Sie wissen nicht wie fortfahren?</p>
    <p class="body-copy"><strong>Ich helfe Ihnen weiter! Denn die Schreibkunst fusst wie alle Künste nicht nur auf Genie, sondern in erster Linie auf Handwerk, dass Ich Ihnen beibringen kann.</strong></p>
    <p class="body-copy">Sie selber lesen gerne und sind dem Schreiben nicht abgewandt. Eine perfekte Rechtschreibung ist nicht nötig, dafür gibt es das gegenseitige Lektorat. Aber sie sollten der deutschen Sprache soweit mächtig sein, dass Sie Haupt, Nebensätze, Fälle und Zeiten meistens korrekt anwenden.</p>
  </section>

  <div class="ornament ornament--url-left" role="img" aria-label="Goldenes Zierornament"></div>
  <p class="web">www.kolibri-stube.ch</p>
  <div class="ornament ornament--url-right" role="img" aria-label="Goldenes Zierornament"></div>

  <div class="portrait" role="img" aria-label="Porträtfoto der Kursleiterin"></div>
  <aside class="trainer">Kursleitung<br><strong>Dr. Lena Varnhold</strong> ist Erwachsenenbildnerin und Lehrerin für Deutsch und spezialisierte sich auf den Unterricht des literarischen Schreibens von Drehbücher, Erzählungen und Romanen. Als Autorin mehrerer Fachbücher und Verlagsleiterin des Falkmoor Verlags kennt Sie auch die Möglichkeiten des Vertriebes und Buchhandels.</aside>

  <div class="logo-box">
    <h1 class="logo-name">Kolibri<br>Stube</h1>
  </div>
  <div class="ornament ornament--logo" role="img" aria-label="Goldenes Eckornament"></div>
  <div class="quill-area" role="img" aria-label="Illustration einer Schreibfeder"></div>
  <p class="tagline"><span>Mit der Kolibri-Stube</span><span>zu Ihrem eigenen Roman</span></p>

  <div class="ornament ornament--corner" role="img" aria-label="Goldenes Eckornament"></div>
</main>
</body>
</html>
```